Property developer, money partner needs business card design using logo concept provided

Our company develops residential properties, does money lends for joint ventures in property deals and finds property deals for other money partners. We have provided a basic logo for you to work from. Any graphic or logo design on the card is to communicate development and finance collaboration. Color choice is not so important for us, but color choice does need to reflect professionalism.

```html
<!DOCTYPE html>
<html lang="en">
<head>
<meta charset="utf-8">
<title>Keystone Property Solutions – Business Card</title>
<link href="https://fonts.googleapis.com/css2?family=Montserrat:wght@700&family=Lato:wght@400;700&display=swap" rel="stylesheet">
<style>
  :root {
    --backdrop: #5a5a5c;
    --card-red: #951a1e;
    --card-white: #f6f6f6;
    --ink-white: #ffffff;
    --ink-dark: #3a3a3a;
    --accent-blue: #1c6fb8;
    --accent-red: #a3191f;
    --rule-red: #b8342f;
    --faint-red: rgba(0,0,0,0.08);
    --faint-grey: rgba(0,0,0,0.05);
  }
  * { margin: 0; padding: 0; box-sizing: border-box; }
  html, body { width: 1200px; height: 900px; overflow: hidden; }
  body { background: var(--backdrop); position: relative; font-family: "Lato", sans-serif; }

  .card {
    position: absolute;
    box-shadow: 0 10px 24px rgba(0,0,0,0.35);
    overflow: hidden;
  }

  /* Front */
  .card-front { left: 110px; top: 70px; width: 560px; height: 320px; background: var(--card-red); }
  .front-decor {
    position: absolute; right: -60px; top: -60px; width: 300px; height: 300px;
    border-radius: 50%; background: var(--faint-red);
  }
  .front-brand { position: absolute; left: 44px; bottom: 48px; color: var(--ink-white); }
  .brand-name {
    font-family: "Montserrat", sans-serif; font-weight: 700;
    font-size: 40px; letter-spacing: 12px; line-height: 1;
  }
  .brand-sub { font-size: 22px; letter-spacing: 5px; margin-top: 6px; }
  .brand-reg { font-size: 14px; letter-spacing: 4px; margin-top: 4px; padding-left: 60px; }

  /* Back */
  .card-back { left: 430px; top: 450px; width: 660px; height: 378px; background: var(--card-white); }
  .back-decor {
    position: absolute; right: -50px; top: -70px; width: 330px; height: 330px;
    border-radius: 50%; background: var(--faint-grey);
  }
  .back-brand { position: absolute; left: 44px; top: 60px; display: flex; align-items: center; gap: 14px; }
  .brand-dot { width: 54px; height: 54px; border-radius: 50%; background: var(--accent-blue); }
  .back-brand .brand-text { color: var(--accent-red); font-family: "Montserrat", sans-serif; font-weight: 700; }
  .back-brand .brand-name { font-size: 28px; letter-spacing: 7px; }
  .back-brand .brand-sub { font-size: 14px; letter-spacing: 3px; margin-top: 4px; }
  .back-brand .brand-reg { font-size: 10px; letter-spacing: 2px; padding-left: 40px; margin-top: 2px; }

  .contact { position: absolute; left: 44px; right: 44px; bottom: 40px; color: var(--ink-dark); }
  .person-name { color: var(--accent-blue); font-weight: 700; font-size: 22px; letter-spacing: 0.5px; }
  .person-role { font-size: 18px; margin-top: 4px; }
  .sep { color: var(--rule-red); padding: 0 5px; }
  .rule { height: 1px; background: var(--rule-red); margin: 12px 0 10px; }
  .details { font-size: 15px; white-space: nowrap; }
</style>
</head>
<body>
  <section class="card card-front">
    <div class="front-decor" aria-hidden="true"></div>
    <div class="front-brand">
      <div class="brand-name">KEYSTONE</div>
      <div class="brand-sub">Property Solutions</div>
      <div class="brand-reg">A.C.N 418 903 226</div>
    </div>
  </section>

  <section class="card card-back">
    <div class="back-decor" aria-hidden="true"></div>
    <div class="back-brand">
      <div class="brand-dot" aria-hidden="true"></div>
      <div class="brand-text">
        <div class="brand-name">KEYSTONE</div>
        <div class="brand-sub">Property Solutions</div>
        <div class="brand-reg">A.C.N 418 903 226</div>
      </div>
    </div>
    <div class="contact">
      <div class="person-name">ALEX MORGAN</div>
      <div class="person-role">Director<span class="sep">|</span>T. 300-555-0142</div>
      <div class="rule"></div>
      <div class="details">E. info@keystoneps.com<span class="sep">|</span>W. www.keystoneps.com<span class="sep">|</span>00 dummy city, Place 0000</div>
    </div>
  </section>
</body>
</html>
```